The name of the company is Torvend Holdings, LLC. I would like a business card with a logo.

On the top left, I would like a logo design of a crown and I would like Torvend over the top of the crown while Holdings on the bottom. Please see attached files as an example of crown and positioning of Torvend Holdings. Then I would like the letters TH in the middle(see picture).

Colors

Designer to choose colors to be used in the design.

```html
<!DOCTYPE html>
<html lang="en">
<head>
<meta charset="utf-8">
<title>Torvend Holdings – Business Card</title>
<link href="https://fonts.googleapis.com/css2?family=Open+Sans:wght@400;600&family=Noto+Serif:wght@400;700&display=swap" rel="stylesheet">
<style>
  :root {
    --backdrop: #d6d6d6;
    --card: #ffffff;
    --ink: #2e2e2e;
    --ink-soft: #555555;
    --brand-red: #a8161d;
    --brand-green: #2f8a3e;
    --mark-faint: #f3e6e4;
  }
  * { margin: 0; padding: 0; box-sizing: border-box; }
  html, body {
    width: 1200px; height: 915px; overflow: hidden;
    background: var(--backdrop);
  }
  .canvas { position: relative; width: 1200px; height: 915px; }

  .card {
    position: absolute; top: 309px;
    width: 520px; height: 297px;
    background: var(--card);
    box-shadow: 0 6px 18px rgba(0,0,0,0.18);
    overflow: hidden;
  }
  .card--front { left: 60px; }
  .card--back { left: 620px; }

  .wordmark {
    display: flex; align-items: center; gap: 10px;
    font-family: "Open Sans", sans-serif;
    font-weight: 600; letter-spacing: 0.12em;
    color: var(--ink); text-transform: uppercase;
  }
  .wordmark__dot {
    width: 14px; height: 14px; border-radius: 50%;
    background: var(--brand-red); flex: none;
  }
  .card--front .wordmark {
    position: absolute; left: 30px; top: 34px; font-size: 17px;
  }
  .card--back .wordmark {
    position: absolute; left: 0; right: 0; top: 134px;
    justify-content: center; font-size: 19px;
  }

  .contact {
    position: absolute; left: 30px; top: 98px;
    font-family: "Noto Serif", serif; font-size: 11px;
    line-height: 1.55; color: var(--ink-soft);
  }
  .contact__label { font-weight: 700; color: var(--brand-red); }

  .identity {
    position: absolute; left: 330px; top: 96px;
    font-family: "Noto Serif", serif; color: var(--ink);
  }
  .identity__name { font-size: 14px; }
  .identity__title { font-size: 10.5px; color: var(--ink-soft); margin-top: 2px; }

  .mark-decoration {
    position: absolute; left: 230px; top: 150px;
    width: 200px; height: 130px; border-radius: 40px;
    background: radial-gradient(ellipse at center, var(--mark-faint) 0%, rgba(243,230,228,0.35) 70%, rgba(255,255,255,0) 100%);
  }

  .edge-band {
    position: absolute; left: 0; right: 0; bottom: 10px;
    height: 5px; background: var(--brand-red);
  }
</style>
</head>
<body>
<main class="canvas">
  <section class="card card--front" aria-label="Business card front">
    <div class="wordmark"><span class="wordmark__dot"></span>Torvend Holdings</div>

    <address class="contact">
      418 Larkmoor Drive, Suite 200<br>
      Fernbrook Hills, CA 90512<br>
      <span class="contact__label">Tel:</span> (310) 555-0148<br>
      Dkellwyn.Holdings@mailbox.com
    </address>

    <div class="identity">
      <p class="identity__name">Dara Kellwyn, MBA</p>
      <p class="identity__title">Founder/CEO</p>
    </div>

    <div class="mark-decoration" role="img" aria-label="Faint enlarged brand mark decoration"></div>
    <div class="edge-band"></div>
  </section>

  <section class="card card--back" aria-label="Business card back">
    <div class="wordmark"><span class="wordmark__dot"></span>Torvend Holdings</div>
  </section>
</main>
</body>
</html>
```